Wool Product Label / Yarn Band

Looking to update the packaging on our wool products. This includes a design for a paper band to place around braided wool or yarn, and a design for a sticker to place on the outside of tissue paper wrapping. Open to updating or modifying the logo, which does not fit well on a round sticker, but the sticker could also be something wool related (like a sheep or drop spindle) that does not include the logo.
Target Market(s)
Wool crafters (knitters / spinners / felters). Mainly women, aged 30-70
Industry/Entity Type
Textile
Colors
Designer to choose colors to be used in the design.
Requirements
Must have
- Band needs to include, brand name, logo, url (fernloomstead.com), dyelot number, as well as the fiber content (ex: Merino Wool) and weight of the fiber (ex: 4oz).
Nice to have
- Band would ideally be easily customized because the weight and fiber content is variable and will be printed specifically for each product, Variable information can be on a sticker or printed directly on a band that can be printed on a standard printer. Attached is a photo of the current band and it's application.

```html
<!DOCTYPE html>
<html lang="en">
<head>
<meta charset="utf-8">
<title>Fernloomstead Yarn Band</title>
<link rel="stylesheet" href="https://fonts.googleapis.com/css2?family=Lato:wght@400;700&family=Roboto+Condensed:wght@400;700&display=swap">
<style>
  :root {
    --page: #e6e6e8;
    --ink: #58585b;
    --frame-dark: #4a4a4d;
    --tab-dark: #4d4d50;
    --brand-green: #6cb944;
    --paper: #ffffff;
    --knit-warm: #f6d58f;
    --knit-yellow: #eef0a2;
    --knit-green: #cde5a6;
    --knit-aqua: #b3dfdc;
    --band-olive: #b4b232;
    --band-green: #5b9f3b;
    --band-teal: #2e7b6c;
    --band-blue: #23688e;
  }
  html, body {
    margin: 0;
    padding: 0;
    width: 1200px;
    height: 403px;
    overflow: hidden;
    background: var(--page);
  }
  .yarn-band {
    position: absolute;
    left: 64px;
    top: 63px;
    width: 1073px;
    height: 276px;
  }
  .yarn-band svg { display: block; }
  .label-text { font-family: "Lato", Arial, sans-serif; fill: var(--ink); font-weight: 700; }
  .brand-name { font-family: "Roboto Condensed", "Arial Narrow", sans-serif; font-weight: 700; fill: var(--brand-green); }
  .tagline { font-family: "Roboto Condensed", "Arial Narrow", sans-serif; font-weight: 400; fill: var(--ink); }
  .spec-text { font-family: "Lato", Arial, sans-serif; font-weight: 700; fill: var(--paper); }
</style>
</head>
<body>
  <div class="yarn-band">
    <svg width="1073" height="276" viewBox="0 0 1073 276" xmlns="http://www.w3.org/2000/svg">
      <defs>
        <linearGradient id="knitTones" x1="0" y1="0" x2="1" y2="0">
          <stop offset="0" stop-color="var(--knit-warm)"/>
          <stop offset="0.35" stop-color="var(--knit-yellow)"/>
          <stop offset="0.7" stop-color="var(--knit-green)"/>
          <stop offset="1" stop-color="var(--knit-aqua)"/>
        </linearGradient>
        <linearGradient id="bandTones" x1="0" y1="0" x2="1073" y2="0" gradientUnits="userSpaceOnUse">
          <stop offset="0" stop-color="var(--band-olive)"/>
          <stop offset="0.35" stop-color="var(--band-green)"/>
          <stop offset="0.7" stop-color="var(--band-teal)"/>
          <stop offset="1" stop-color="var(--band-blue)"/>
        </linearGradient>
      </defs>

      <rect class="knit-pattern" x="0" y="0" width="1073" height="276" fill="url(#knitTones)" role="img" aria-label="Pastel knitted stitch pattern background"/>

      <g class="frame-outline" fill="none" stroke="var(--frame-dark)" stroke-width="26" stroke-linejoin="round">
        <path d="M30,81 L1043,81 L1010,137 L1043,193 L30,193 L63,137 Z"/>
        <ellipse cx="536" cy="138" rx="232" ry="125"/>
      </g>
      <g class="frame-colour" fill="none" stroke="url(#bandTones)" stroke-width="14" stroke-linejoin="round">
        <path d="M30,81 L1043,81 L1010,137 L1043,193 L30,193 L63,137 Z"/>
        <ellipse cx="536" cy="138" rx="232" ry="125"/>
      </g>
      <g class="frame-paper" fill="var(--paper)">
        <path d="M30,81 L1043,81 L1010,137 L1043,193 L30,193 L63,137 Z"/>
        <ellipse cx="536" cy="138" rx="232" ry="125"/>
      </g>

      <text class="label-text dyelot" x="92" y="143" font-size="17">S/N: MER/SILK-BLEND1</text>
      <text class="label-text website" x="988" y="143" font-size="17" text-anchor="end">www.fernloomstead.com</text>

      <text class="brand-name" x="536" y="119" font-size="54" text-anchor="middle">fernloomstead</text>
      <text class="tagline" x="574" y="165" font-size="22" text-anchor="middle">hand painted yarn &amp; fibers</text>

      <path class="spec-tab" d="M379,182 L694,182 L678,206 Q669,220 655,220 L418,220 Q404,220 396,206 Z" fill="var(--tab-dark)"/>
      <path class="qty-tab" d="M471,219 L601,219 L585,239 Q579,247 569,247 L504,247 Q494,247 488,239 Z" fill="var(--tab-dark)"/>
      <text class="spec-text fiber-content" x="536" y="207" font-size="17" text-anchor="middle">85% Merino Wool | 15% Silk</text>
      <text class="spec-text fiber-weight" x="536" y="239" font-size="17" text-anchor="middle">Qty: 4oz</text>
    </svg>
  </div>
</body>
</html>
```